Name our house

My wife and I just moved to a new house. We asked friends to suggest a name based on what they know about us and our interests. The winner was "The Birches": based on our love of sailing (ie leeward vs windward) and our love of champagne (ie the yeast sediment during secondary fermentation); our name is not Birch.
We want a design we can use for a name sign at the streetfront to our house. We will have it laser cut and etched from aluminium sheet so should be single colour (probably powder coated black).
We would like the name combined with some kind of relevant imagery on the sign.
The house is about 1910 design, but clean modern lines are also a possibility.
Reason: We have been away for a week, unable to provide any useful feedback in the interim, so need to extend our deadline.

```html
<!DOCTYPE html>
<html lang="en">
<head>
<meta charset="utf-8">
<title>The Birches – House Name Sign</title>
<link rel="stylesheet" href="https://fonts.googleapis.com/css2?family=Elsie+Swash+Caps:wght@400;900&display=swap">
<style>
  :root {
    --page: #ffffff;
    --plate: #1b1b1b;
    --plate-grain: #2a2a2a;
    --etch: #ffffff;
    --etch-soft: #d9d9d9;
  }
  html, body {
    margin: 0;
    padding: 0;
    overflow: hidden;
  }
  body {
    width: 1125px;
    height: 1200px;
    background: var(--page);
    position: relative;
    font-family: "Elsie Swash Caps", serif;
  }
  .sign-plate {
    position: absolute;
    left: 62px;
    top: 220px;
    width: 1000px;
    height: 760px;
    clip-path: polygon(0 13%, 18% 3%, 82% 3%, 100% 13%, 100% 87%, 82% 97%, 18% 97%, 0 87%);
    background:
      repeating-linear-gradient(90deg, var(--plate) 0 2px, var(--plate-grain) 2px 3px, var(--plate) 3px 6px),
      var(--plate);
  }
  .house-number,
  .house-name {
    position: absolute;
    left: 0;
    width: 100%;
    margin: 0;
    text-align: center;
    color: var(--etch);
    font-weight: 900;
    line-height: 1;
  }
  .house-number {
    top: 105px;
    font-size: 200px;
  }
  .house-name {
    top: 385px;
    font-size: 132px;
  }
  .motif {
    position: absolute;
    background: linear-gradient(160deg, var(--etch) 0%, var(--etch-soft) 100%);
    opacity: 0.9;
  }
  .motif-champagne {
    left: 30px;
    top: 160px;
    width: 225px;
    height: 175px;
    border-radius: 12px;
  }
  .motif-sailboat {
    left: 690px;
    top: 175px;
    width: 230px;
    height: 210px;
    border-radius: 12px;
  }
  .motif-flourish {
    left: 345px;
    top: 590px;
    width: 310px;
    height: 62px;
    border-radius: 8px;
  }
  .base-rule {
    position: absolute;
    left: 107px;
    top: 662px;
    width: 763px;
    height: 4px;
    background: var(--etch);
  }
</style>
</head>
<body>
  <div class="sign-plate">
    <div class="motif motif-champagne" role="img" aria-label="Two champagne flutes clinking with rising bubbles"></div>
    <div class="motif motif-sailboat" role="img" aria-label="Sailboat with pennant on the water"></div>
    <p class="house-number">26</p>
    <p class="house-name">The Birches</p>
    <div class="motif motif-flourish" role="img" aria-label="Symmetrical scrollwork flourish"></div>
    <div class="base-rule"></div>
  </div>
</body>
</html>
```